Residential Remodeling Contractor needs updated business card

I need a new design for my business card.
Name of the company is Brookfell Construction. I need a card that commands presence, strength, integrity. I have been in business for 28 years. I am a Residential Remodeling Contractor that covers all aspects of a residential remodel and build.

```html
<!DOCTYPE html>
<html lang="en">
<head>
<meta charset="UTF-8">
<title>Brookfell Construction – Business Card</title>
<link rel="stylesheet" href="https://fonts.googleapis.com/css2?family=Montserrat:wght@400;500;700&display=swap">
<style>
  :root {
    --brand-blue: #213f80;
    --brand-deep: #142c66;
    --ink-blue: #1f3a85;
    --ink-dark: #1a1a1a;
    --paper: #ffffff;
    --backdrop: #d9dadc;
    --on-blue: #ffffff;
  }
  * { margin: 0; padding: 0; box-sizing: border-box; }
  html, body { width: 1200px; height: 900px; overflow: hidden; }
  body {
    background: var(--backdrop);
    font-family: "Montserrat", Arial, sans-serif;
    position: relative;
  }
  .card {
    position: absolute;
    left: 250px;
    width: 700px;
    height: 400px;
    overflow: hidden;
    box-shadow: 0 6px 18px rgba(0,0,0,0.18);
  }
  /* Back side */
  .card-back {
    top: 40px;
    background: var(--brand-blue);
    color: var(--on-blue);
  }
  .card-back .wordmark {
    position: absolute;
    top: 150px;
    left: 0;
    width: 100%;
    display: flex;
    justify-content: center;
    align-items: center;
    gap: 14px;
    font-weight: 700;
    font-size: 32px;
    letter-spacing: 2px;
    text-transform: uppercase;
    color: var(--brand-deep);
    white-space: nowrap;
  }
  .card-back .wordmark .mark-square {
    width: 18px; height: 18px; background: var(--brand-deep); flex: none;
  }
  .card-back .tagline {
    position: absolute;
    top: 300px;
    left: 0;
    width: 100%;
    text-align: center;
    font-weight: 500;
    font-size: 15px;
    letter-spacing: 1.5px;
    text-transform: uppercase;
  }
  /* Front side */
  .card-front {
    top: 470px;
    background: var(--paper);
  }
  .card-front .accent-bar {
    position: absolute;
    left: 0; top: 44px;
    width: 28px; height: 34px;
    background: var(--brand-blue);
  }
  .card-front .holder-name {
    position: absolute;
    left: 56px; top: 42px;
    font-weight: 700;
    font-size: 26px;
    letter-spacing: 1px;
    color: var(--ink-blue);
    text-transform: uppercase;
  }
  .card-front .holder-role {
    position: absolute;
    left: 56px; top: 76px;
    font-size: 15px;
    color: var(--ink-dark);
  }
  .card-front .contact-list {
    position: absolute;
    left: 48px; top: 252px;
    list-style: none;
    font-size: 18px;
    color: var(--ink-dark);
    line-height: 26px;
  }
  .card-front .contact-list li { display: flex; align-items: center; gap: 6px; }
  .card-front .contact-list svg { width: 15px; height: 15px; flex: none; }
  .card-front .contact-list .web-domain { color: var(--ink-blue); }
  .card-front .address {
    position: absolute;
    left: 40px; top: 340px;
    font-size: 18px;
    letter-spacing: 0.5px;
    color: var(--ink-dark);
  }
  .card-front .wordmark {
    position: absolute;
    right: 44px; top: 196px;
    display: flex;
    align-items: center;
    gap: 12px;
    font-weight: 700;
    font-size: 24px;
    line-height: 30px;
    letter-spacing: 1.2px;
    text-transform: uppercase;
    color: var(--ink-blue);
    white-space: nowrap;
  }
  .card-front .wordmark .mark-square {
    width: 16px; height: 16px; background: var(--ink-blue); flex: none;
  }
</style>
</head>
<body>
  <section class="card card-back">
    <div class="wordmark"><span class="mark-square"></span><span>Brookfell Construction</span></div>
    <p class="tagline">I have been in business for 28 years</p>
  </section>

  <section class="card card-front">
    <span class="accent-bar"></span>
    <h1 class="holder-name">Marcus Devane</h1>
    <p class="holder-role">Director</p>

    <ul class="contact-list">
      <li>
        <svg viewBox="0 0 16 16" aria-hidden="true"><path d="M4 1.5 L6.5 5 L5 6.5 Q6.5 9.5 9.5 11 L11 9.5 L14.5 12 L12.5 14.5 Q5 13 1.5 3.5 Z" fill="none" stroke="#1f3a85" stroke-width="1.4"/></svg>
        (555) 014-2290
      </li>
      <li>
        <svg viewBox="0 0 16 16" aria-hidden="true"><rect x="1.5" y="3.5" width="13" height="9" fill="none" stroke="#1f3a85" stroke-width="1.4"/><path d="M1.5 3.5 L8 9 L14.5 3.5" fill="none" stroke="#1f3a85" stroke-width="1.4"/></svg>
        info@brookfellbuild.com
      </li>
      <li>
        <svg viewBox="0 0 16 16" aria-hidden="true"><circle cx="8" cy="8" r="6.5" fill="none" stroke="#1f3a85" stroke-width="1.3"/><ellipse cx="8" cy="8" rx="3" ry="6.5" fill="none" stroke="#1f3a85" stroke-width="1.1"/><path d="M1.5 8 H14.5 M2.5 5 H13.5 M2.5 11 H13.5" stroke="#1f3a85" stroke-width="1"/></svg>
        <span>www.<span class="web-domain">brookfellbuild</span>.com</span>
      </li>
    </ul>
    <p class="address">48 Millbrook Lane Cedarton, GA 30990</p>

    <div class="wordmark"><span class="mark-square"></span><span>Brookfell<br>Construction</span></div>
  </section>
</body>
</html>
```